North Maple Ridge (by the numbers)

We (city communications office of North Maple Ridge, Arkansas) are launching a magazine to be delivered to every house in the community. We would like the first inside page to be an infographic of the important and interesting "numbers" from 2017. We want it to be visually interesting and convey the huge amount of important services we provide our residents. I have included a document with the relevant statistics to be used.

Target Market(s)

Residents of our city

Industry/Entity Type

House

Colors

Designer to choose colors to be used in the design.

Requirements
Must have
• Our logo must be prominent. The dimensions should be able to fit onto a standard full page magazine. If the infographic is best displayed on two pages we will accept that as well, and change our layout.
Nice to have
• Not every statistic we have provided must be used but if they can be, that is preferable. I have also included some inspirational infographics that appealed to me and inspired the idea, but I am excited about new concepts that might not look anything like those that I have provided.
Should not have
• The design should not have anything incorporated that cannot be presented to families in our community. It must be all ages friendly.

```html
<!DOCTYPE html>
<html lang="en">
<head>
<meta charset="utf-8">
<title>North Maple Ridge by the Numbers 2017</title>
<link href="https://fonts.googleapis.com/css2?family=Source+Sans+3:wght@600;700&display=swap" rel="stylesheet">
<style>
  :root{
    --page:#e9e9e9;
    --navy-dark:#222d54;
    --navy:#1e4a9a;
    --white:#ffffff;
    --sky-top:#d8eef9;
    --sky-bottom:#58bde8;
    --city:#8c8c8c;
    --orange:#f5a31b;
    --orange-dark:#e98a12;
    --red:#c8202f;
    --red-dark:#9e1622;
    --green:#8cc63f;
    --green-dark:#6ea52c;
    --teal:#1fb5c9;
    --teal-dark:#1a8a99;
    --coral:#ef5a4c;
    --navy-mid:#2a3a6f;
    --navy-deep:#1f2a55;
  }
  html,body{margin:0;width:1200px;height:1000px;overflow:hidden;background:var(--page);}
  .canvas{position:absolute;left:0;top:37px;width:1200px;height:925px;display:block;}
  svg text{font-family:"Source Sans 3",sans-serif;font-weight:600;fill:var(--white);}
  .title{font-size:28px;font-weight:700;}
  .subtitle{font-size:22px;}
  .year{font-size:56px;font-weight:700;}
  .brand{font-size:17px;font-weight:700;fill:var(--navy);}
  .label{font-size:21px;}
  .label-sm{font-size:17px;}
  .figure{font-size:17px;}
  .figure-sm{font-size:13px;}
  .navy-dark{fill:var(--navy-dark);} .navy{fill:var(--navy);}
  .orange{fill:var(--orange);} .orange-dark{fill:var(--orange-dark);}
  .red{fill:var(--red);} .red-dark{fill:var(--red-dark);}
  .green{fill:var(--green);} .green-dark{fill:var(--green-dark);}
  .teal{fill:var(--teal);} .teal-dark{fill:var(--teal-dark);}
  .coral{fill:var(--coral);}
  .navy-mid{fill:var(--navy-mid);} .navy-deep{fill:var(--navy-deep);}
  .art{opacity:.85;}
</style>
</head>
<body>
<svg class="canvas" viewBox="0 0 952 734" xmlns="http://www.w3.org/2000/svg">
  <defs>
    <linearGradient id="sky" x1="0" y1="0" x2="0" y2="1">
      <stop offset="0" stop-color="var(--sky-top)"/>
      <stop offset="1" stop-color="var(--sky-bottom)"/>
    </linearGradient>
    <linearGradient id="cityTone" x1="0" y1="0" x2="0" y2="1">
      <stop offset="0" stop-color="#9a9a9a"/>
      <stop offset="1" stop-color="#7f7f7f"/>
    </linearGradient>
  </defs>

  <!-- sky -->
  <rect class="sky" x="0" y="94" width="952" height="640" fill="url(#sky)"/>
  <g role="img" aria-label="Grey city skyline silhouette along the bottom">
    <rect x="0" y="590" width="952" height="144" fill="url(#cityTone)" opacity=".75"/>
    <rect x="0" y="690" width="952" height="44" fill="var(--city)"/>
  </g>

  <!-- header -->
  <g class="header">
    <rect class="navy-dark" x="0" y="0" width="686" height="94"/>
    <rect class="navy" x="686" y="0" width="266" height="94"/>
    <text class="title" x="430" y="45" text-anchor="middle">North Maple Ridge (NMR)</text>
    <text class="subtitle" x="430" y="73" text-anchor="middle">by the Numbers</text>
    <text class="year" x="820" y="67" text-anchor="middle">2017</text>
  </g>

  <!-- brand block -->
  <g class="brand-block">
    <rect x="60" y="0" width="142" height="114" fill="var(--white)"/>
    <circle cx="131" cy="30" r="12" fill="var(--navy)"/>
    <text class="brand" x="131" y="64" text-anchor="middle">North Maple</text>
    <text class="brand" x="131" y="84" text-anchor="middle">Ridge</text>
  </g>

  <!-- LEFT COLUMN -->
  <!-- population -->
  <g class="stat">
    <rect class="art" role="img" aria-label="Illustration of two residents standing side by side" x="112" y="145" width="82" height="98" rx="8" fill="#3b5fa8"/>
    <polygon class="orange-dark" points="340,146 370,140 362,152 340,152"/>
    <polygon class="orange" points="222,152 370,152 370,200 222,200 200,176"/>
    <text class="label" x="298" y="184" text-anchor="middle">Population</text>
    <circle class="navy-deep" cx="407" cy="210" r="42"/>
    <path class="navy-mid" d="M407,168 A42,42 0 0 0 407,252 Z"/>
    <text class="figure" x="407" y="216" text-anchor="middle">65,004</text>
  </g>

  <!-- police calls -->
  <g class="stat">
    <rect class="art" role="img" aria-label="Illustration of a red emergency siren light" x="125" y="262" width="66" height="66" rx="10" fill="var(--red)"/>
    <polygon class="red-dark" points="355,258 382,252 376,265 355,265"/>
    <polygon class="red" points="232,265 388,265 388,313 232,313 210,289"/>
    <text class="label" x="304" y="297" text-anchor="middle">Police 911 calls</text>
    <circle class="orange" cx="405" cy="318" r="33"/>
    <path class="orange-dark" d="M405,285 A33,33 0 0 1 405,351 Z"/>
    <text class="figure-sm" x="405" y="323" text-anchor="middle">26,660</text>
  </g>

  <!-- asphalt -->
  <g class="stat">
    <rect class="art" role="img" aria-label="Illustration of an orange dump truck on a road tile" x="85" y="352" width="144" height="90" rx="8" fill="#e98a2a"/>
    <polygon class="navy-deep" points="440,358 470,352 464,365 440,365"/>
    <polygon class="navy" points="238,365 470,365 470,440 238,440 218,402"/>
    <text class="label-sm" x="350" y="388" text-anchor="middle">Tons of asphalt used in</text>
    <text class="label-sm" x="350" y="408" text-anchor="middle">repairing potholes and</text>
    <text class="label-sm" x="350" y="428" text-anchor="middle">street overlays</text>
    <circle class="teal" cx="452" cy="450" r="33"/>
    <path class="teal-dark" d="M452,417 A33,33 0 0 0 452,483 Z"/>
    <text class="figure-sm" x="452" y="455" text-anchor="middle">5,952</text>
  </g>

  <!-- tires -->
  <g class="stat">
    <rect class="art" role="img" aria-label="Illustration of three recycling bins in green, yellow and red" x="65" y="470" width="160" height="70" rx="8" fill="#8a9a3a"/>
    <polygon class="orange-dark" points="395,487 424,481 418,493 395,493"/>
    <polygon class="orange" points="248,493 442,493 442,540 248,540 228,516"/>
    <text class="label" x="342" y="524" text-anchor="middle">Used tires recycled</text>
    <circle class="navy-deep" cx="447" cy="543" r="30"/>
    <path class="navy" d="M447,513 A30,30 0 0 0 447,573 Z"/>
    <text class="figure-sm" x="447" y="548" text-anchor="middle">4,221</text>
  </g>

  <!-- parks -->
  <g class="stat">
    <rect class="art" role="img" aria-label="Illustration of an isometric park tile with trees and benches" x="40" y="560" width="164" height="128" rx="10" fill="#7cb342"/>
    <polygon class="red-dark" points="410,588 438,582 432,594 410,594"/>
    <polygon class="red" points="225,594 432,594 432,642 225,642 205,618"/>
    <text class="label" x="322" y="625" text-anchor="middle">Neighborhood parks</text>
    <circle class="orange" cx="458" cy="632" r="30"/>
    <path class="orange-dark" d="M458,602 A30,30 0 0 1 458,662 Z"/>
    <text class="figure-sm" x="458" y="637" text-anchor="middle">34</text>
  </g>

  <!-- RIGHT COLUMN -->
  <!-- park visitors -->
  <g class="stat">
    <rect class="art" role="img" aria-label="Illustration of a grassy tile with three trees" x="505" y="120" width="145" height="88" rx="8" fill="#6ea52c"/>
    <polygon class="green-dark" points="826,131 856,125 850,138 826,138"/>
    <polygon class="green" points="665,138 872,138 872,185 665,185 645,161"/>
    <text class="label" x="762" y="170" text-anchor="middle">Visitors to Alder Park</text>
    <circle class="teal" cx="878" cy="200" r="30"/>
    <path class="teal-dark" d="M878,170 A30,30 0 0 0 878,230 Z"/>
    <text class="figure-sm" x="878" y="205" text-anchor="middle">779,621</text>
  </g>

  <!-- fire calls -->
  <g class="stat">
    <rect class="art" role="img" aria-label="Illustration of a red fire hydrant" x="580" y="222" width="68" height="96" rx="10" fill="#b3242a"/>
    <polygon class="orange-dark" points="792,238 822,232 816,245 792,245"/>
    <polygon class="orange" points="675,245 822,245 822,290 675,290 655,267"/>
    <text class="label" x="743" y="276" text-anchor="middle">Fire 911 calls</text>
    <circle class="coral" cx="837" cy="287" r="30"/>
    <path class="red" d="M837,257 A30,30 0 0 0 837,317 Z"/>
    <text class="figure-sm" x="837" y="292" text-anchor="middle">12,560</text>
  </g>

  <!-- garbage -->
  <g class="stat">
    <rect class="art" role="img" aria-label="Illustration of an orange garbage truck on a road tile" x="520" y="340" width="140" height="85" rx="8" fill="#f08c2a"/>
    <polygon class="teal-dark" points="832,338 862,332 856,345 832,345"/>
    <polygon class="teal" points="670,345 862,345 862,395 670,395 650,370"/>
    <text class="label-sm" x="760" y="366" text-anchor="middle">Tons of Household</text>
    <text class="label-sm" x="760" y="386" text-anchor="middle">garbage collected</text>
    <circle class="green" cx="870" cy="402" r="30"/>
    <path class="green-dark" d="M870,372 A30,30 0 0 0 870,432 Z"/>
    <text class="figure-sm" x="870" y="407" text-anchor="middle">16,768</text>
  </g>

  <!-- green waste -->
  <g class="stat">
    <rect class="art" role="img" aria-label="Illustration of a yellow shed with yard waste bags" x="525" y="474" width="125" height="76" rx="8" fill="#e6b52a"/>
    <polygon class="green-dark" points="866,448 896,442 890,455 866,455"/>
    <polygon class="green" points="635,455 900,455 900,503 635,503 615,479"/>
    <text class="label-sm" x="765" y="476" text-anchor="middle">Cubic yards of green (yard)</text>
    <text class="label-sm" x="765" y="496" text-anchor="middle">waste collected</text>
    <circle class="orange" cx="868" cy="514" r="30"/>
    <path class="orange-dark" d="M868,484 A30,30 0 0 1 868,544 Z"/>
    <text class="figure-sm" x="868" y="519" text-anchor="middle">116,675</text>
  </g>

  <!-- inclusive playgrounds -->
  <g class="stat">
    <rect class="art" role="img" aria-label="Illustration of an isometric playground tile with trees and play equipment" x="505" y="575" width="145" height="115" rx="10" fill="#7cb342"/>
    <polygon class="navy-deep" points="866,593 896,587 890,600 866,600"/>
    <polygon class="navy" points="680,600 900,600 900,670 680,670 660,635"/>
    <text class="label-sm" x="782" y="620" text-anchor="middle">Open Hands Inclusive</text>
    <text class="label-sm" x="782" y="640" text-anchor="middle">Playgrounds built for kids</text>
    <text class="label-sm" x="782" y="660" text-anchor="middle">with special needs</text>
    <circle class="teal" cx="887" cy="677" r="28"/>
    <path class="teal-dark" d="M887,649 A28,28 0 0 0 887,705 Z"/>
    <text class="figure" x="887" y="683" text-anchor="middle">1</text>
  </g>
</svg>
</body>
</html>
```